ZEPRILO.COM is a premium domain sales company. Our competitors are companies like vastplots.example, getparcels.example, peerwords.example. Our current site is at www.zeprilos.example.

We want to have the ability to search for domains, to highlight special offers and have some testimonials on the index page.

The logo for the site is attached.

Please be sure that the order form fits on the screen without scrolling the page. I want the entire form, including the submit button to fit without any page scrolling.

Delivered product - INDEX PAGE, ORDER FORM AND CONTENT PAGE PSDs.

Target Market(s)

Small to Medium business professionals

Industry/Entity Type

It Company

Requirements
Must have
• 1. List of domains for sale
2. Simple search box with button to run the search
3. link for advanced search
4. testimonial area. Note - this can be a small box where a different testimonial is displayed on each page load.
Nice to have
• Would like the site to have some white space. Don't want a heavily packed website. Give it an "airy" feel.

```html
<!DOCTYPE html>
<html lang="en">
<head>
<meta charset="utf-8">
<title>ZEPRILO.COM – Find Your Domain</title>
<link rel="stylesheet" href="https://fonts.googleapis.com/css2?family=Montserrat:wght@700;800&family=Open+Sans:wght@400;600;700&family=Cabin:wght@400;600&display=swap">
<style>
:root{
  --blue:#1d5aa6;
  --blue-dark:#17457f;
  --navy:#102a4c;
  --navy-deep:#0c203b;
  --green:#6cb41e;
  --green-dark:#4f8d10;
  --green-text:#1f7a3a;
  --ink:#333;
  --muted:#777;
  --line:#dcdcdc;
  --page:#eeeeee;
  --white:#fff;
}
*{margin:0;padding:0;box-sizing:border-box}
html,body{width:819px;height:1200px;overflow:hidden}
body{position:relative;background:var(--page);font-family:"Open Sans",sans-serif;color:var(--ink)}
.abs{position:absolute}

/* top bar */
.topbar{left:0;top:0;width:819px;height:21px;background:var(--blue);border-bottom:1px solid var(--blue-dark);font-size:7.5px;color:var(--white)}
.topbar .cell{position:absolute;top:0;height:21px;display:flex;align-items:center;gap:5px}
.topbar .divider{position:absolute;top:0;width:1px;height:21px;background:rgba(255,255,255,.25)}
.social{display:flex;gap:3px}
.social span{width:12px;height:12px;border-radius:50%;background:#3d78c4;display:block}

/* header */
.header{left:0;top:21px;width:819px;height:54px;background:var(--white)}
.logo{position:absolute;left:126px;top:15px;display:flex;align-items:center;gap:6px;font-family:"Open Sans",sans-serif;font-weight:700;font-size:24px;color:var(--blue);letter-spacing:-.5px}
.logo .dot{width:14px;height:14px;border-radius:50%;background:var(--green)}
.nav{position:absolute;right:126px;top:20px;display:flex;gap:17px;font-size:9.5px;color:#8a8a8a;text-transform:uppercase}
.nav a{color:inherit;text-decoration:none;line-height:18px}
.nav a.active{background:var(--green);color:var(--white);padding:0 9px;border:1px solid var(--green-dark)}

/* hero */
.hero{left:0;top:75px;width:819px;height:371px;overflow:hidden}
.hero-bg{position:absolute;inset:0;background:radial-gradient(ellipse at 50% 35%,#7a2e1c 0%,#4a1d14 40%,#2a1610 80%)}
.advanced{position:absolute;left:654px;top:0;width:44px;text-align:center;font-family:Cabin,sans-serif;font-size:9px;color:#c8b9b0;line-height:1.1}
.hero h1{position:absolute;left:0;top:20px;width:819px;text-align:center;font-family:Montserrat,sans-serif;font-weight:800;font-size:37px;color:var(--white);letter-spacing:.5px}
.hero h1 em{font-style:normal;color:var(--green)}
.hero h2{position:absolute;left:0;top:60px;width:819px;text-align:center;font-family:Cabin,sans-serif;font-weight:400;font-size:26px;color:var(--white)}
.hero .intro{position:absolute;left:225px;top:95px;width:369px;text-align:center;font-size:7.4px;line-height:1.25;color:#eee}
.search{position:absolute;left:185px;top:135px;width:259px;height:29px;background:var(--white);border-radius:2px;display:flex;align-items:center}
.search .placeholder{padding-left:11px;font-size:12.5px;color:#b3b3b3;flex:1}
.search .tld{width:63px;height:21px;margin-right:4px;border:1px solid #ccc;border-radius:2px;background:linear-gradient(#fff,#e6e6e6);font-size:9.5px;color:#777;display:flex;align-items:center;justify-content:space-around;font-weight:600}
.search-btn{position:absolute;left:541px;top:135px;width:90px;height:29px;background:linear-gradient(#8fd13a,#62a816);border:1px solid var(--green-dark);border-radius:2px;font-family:Montserrat,sans-serif;font-weight:700;font-size:13px;color:#2d4d08;text-align:center;line-height:27px}
.quote{position:absolute;top:195px;width:270px;height:45px;background:rgba(20,10,8,.55);font-size:7.2px;line-height:1.45;color:#eee;padding:7px 10px 0 36px}
.quote::before{content:"\201C";position:absolute;left:10px;top:-2px;font-size:30px;font-family:Georgia,serif;color:#888}
.quote::after{content:"";position:absolute;left:14px;bottom:-8px;border-right:10px solid transparent;border-top:8px solid rgba(20,10,8,.55)}
.quote-name{position:absolute;top:243px;font-size:7.2px;font-weight:700;color:var(--white);line-height:1.2}
.quote-name small{display:block;font-weight:400;font-size:6.5px;color:#bbb}
.arrows{position:absolute;left:675px;top:258px;font-size:12px;color:#ccc;letter-spacing:2px}

/* features */
.feature{position:absolute;top:387px;width:136px;height:118px;background:var(--white);border-bottom:2px solid var(--blue);box-shadow:0 1px 2px rgba(0,0,0,.2);text-align:center}
.feature .icon{position:absolute;left:50%;top:-20px;margin-left:-19px;width:38px;height:38px;border-radius:50%;background:var(--blue);border:3px solid var(--white);box-shadow:0 0 0 1px #ccc;display:flex;align-items:center;justify-content:center}
.feature h3{margin-top:22px;font-family:Cabin,sans-serif;font-weight:600;font-size:11.5px;line-height:1.2;color:#222}
.feature p{margin:6px 9px 0;font-size:6.3px;line-height:1.45;color:#888}
.feature .more{display:inline-block;margin-top:6px;background:#8c8c8c;color:var(--white);font-size:6.5px;border-radius:6px;padding:1px 9px}

/* welcome */
.welcome-title{left:180px;top:574px;width:245px;text-align:right;font-family:Cabin,sans-serif;font-size:23px;color:#555}
.welcome-title b{font-weight:400;color:var(--green-text)}
.welcome-sub{left:180px;top:612px;width:245px;text-align:right;font-weight:400;font-size:19px;line-height:1.2;color:#9a9a9a}
.cloud-art{left:444px;top:532px;width:192px;height:132px;border-radius:60px 60px 10px 10px;background:linear-gradient(#bfe6f6,#4db7e5)}
.welcome-text{left:165px;top:674px;width:489px;text-align:center;font-size:8.3px;line-height:1.45;color:#666}
.welcome-text a{color:var(--green);text-decoration:none}

/* results */
.results{left:126px;top:756px;width:220px}
.results h4{font-family:Cabin,sans-serif;font-weight:400;font-size:13px;color:var(--green-text)}
.results .lead{font-size:10.5px;color:#888;margin-top:2px}
.stat{margin-top:16px}
.stat .www{font-family:Montserrat,sans-serif;font-weight:700;font-size:13px;color:#444;letter-spacing:1px;display:flex;align-items:center;gap:6px}
.stat .www span{font-size:5px;background:#c7d4e6;color:#567;padding:1px 6px;border-radius:4px;letter-spacing:0}
.stat .num{font-weight:700;font-size:21px;color:var(--blue);line-height:1.1}
.stat .label{font-size:9.5px;color:#888}
.stat-rule{width:190px;height:1px;background:#d6d6d6;margin-top:9px}
.results-divider{left:340px;top:756px;width:1px;height:212px;background:#d6d6d6}
.tabs{left:370px;top:756px;display:flex;font-family:Cabin,sans-serif;font-size:11px}
.tabs span{padding:2px 8px;color:#999}
.tabs .on{background:#e2e2e2;color:#333}
.sales{left:370px;top:786px;width:323px;border-collapse:separate;border-spacing:0 5px;font-size:10px}
.sales th{font-family:Cabin,sans-serif;font-weight:400;font-size:12px;color:#444;background:#e9e9e9;height:27px;border-top:1px solid var(--line);border-bottom:1px solid var(--line)}
.sales td{background:var(--white);height:26px;border-top:1px solid var(--line);border-bottom:1px solid var(--line);color:#888}
.sales td:first-child,.sales th:first-child{padding-left:16px;text-align:left;border-left:1px solid var(--line)}
.sales td:last-child,.sales th:last-child{padding-right:16px;text-align:right;border-right:1px solid var(--line)}
.sales td:first-child{color:var(--green-text)}
.sales td:nth-child(2),.sales th:nth-child(2){text-align:center}
.sales td:last-child{color:var(--blue)}

/* footer */
.footer{left:0;top:1022px;width:819px;height:178px;background:linear-gradient(var(--navy),var(--navy-deep))}
.cta{left:126px;top:997px;width:567px;height:49px;background:var(--white);box-shadow:0 1px 3px rgba(0,0,0,.3)}
.cta h5{position:absolute;left:15px;top:6px;font-family:Cabin,sans-serif;font-weight:400;font-size:16px;color:#333}
.cta p{position:absolute;left:15px;top:29px;font-size:9px;color:#555}
.cta .btn{position:absolute;right:13px;top:12px;width:95px;height:25px;background:var(--green-dark);color:var(--white);font-weight:700;font-size:9.5px;text-align:center;line-height:25px;border-radius:1px}
.fcol{position:absolute;top:1065px;font-size:7px;color:#8b9ab1}
.fcol h6{font-family:Cabin,sans-serif;font-weight:400;font-size:9.5px;color:#c9d3e2;margin-bottom:7px;border-left:2px double #8b9ab1;padding-left:4px}
.fcol ul{list-style:none;padding-left:6px;line-height:1.65}
.fcol address{font-style:normal;padding-left:7px;line-height:1.25}
.fcol address b{color:#c9d3e2;font-weight:600}
.newsletter input{display:block;margin:7px 0 0 6px;width:111px;height:17px;background:#0a1a30;border:1px solid #24406a;color:#6a7b94;font-size:6.5px;padding-left:6px;font-family:inherit}
.newsletter .submit{position:absolute;left:70px;top:67px;width:47px;height:15px;background:linear-gradient(#3b8be0,#1f5fb8);color:var(--white);font-weight:700;font-size:7.5px;text-align:center;line-height:15px;border-radius:2px}
.fsep{position:absolute;top:1065px;width:1px;height:86px;background:rgba(255,255,255,.08)}
.copyright{left:126px;top:1175px;font-size:6px;color:#6d7e97}
.cards{left:475px;top:1173px;display:flex;gap:4px}
.cards span{width:17px;height:11px;border-radius:1px;background:#c9d3e2}
.connect{left:587px;top:1172px;display:flex;align-items:center;gap:3px;font-size:6.5px;color:#8b9ab1}
.connect i{width:13px;height:13px;border-radius:50%;background:#c9d3e2;display:block}
</style>
</head>
<body>

<div class="abs topbar">
  <div class="divider" style="left:125px"></div>
  <div class="cell" style="left:137px">
    <svg width="12" height="10" viewBox="0 0 12 10"><path d="M0 1h2l2 6h6l1.5-4.5H3" fill="none" stroke="#fff" stroke-width="1.2"/><circle cx="5" cy="9" r="1" fill="#fff"/><circle cx="9" cy="9" r="1" fill="#fff"/></svg>
    <span>Cart: 0 Items</span>
  </div>
  <div class="divider" style="left:216px"></div>
  <div class="cell" style="left:419px"><div class="social"><span></span><span></span><span></span><span></span></div></div>
  <div class="divider" style="left:493px"></div>
  <div class="cell" style="left:505px">Register</div>
  <div class="cell" style="left:548px">Login</div>
  <div class="divider" style="left:578px"></div>
  <div class="cell" style="left:590px">
    <svg width="10" height="10" viewBox="0 0 10 10"><path d="M2 0.5l2 2-1 1.3c.6 1.3 1.6 2.3 2.9 2.9L7.2 5.7l2 2L8 9.4C4 9 1 6 .6 2z" fill="#fff"/></svg>
    <span>Call: +1 555.014.2290</span>
  </div>
  <div class="divider" style="left:692px"></div>
</div>

<header class="abs header">
  <div class="logo"><span class="dot"></span>ZEPRILO.COM</div>
  <nav class="nav">
    <a class="active" href="#">Home</a><a href="#">Domains</a><a href="#">FAQs</a><a href="#">About Us</a><a href="#">Contact</a>
  </nav>
</header>

<section class="abs hero">
  <div class="hero-bg" role="img" aria-label="Blurred warm bokeh lights background photo"></div>
  <div class="advanced">
    <svg width="12" height="30" viewBox="0 0 12 30"><path d="M6 0v6M3 8h6v4H3zM6 12v16" stroke="#c8b9b0" stroke-width="1.3" fill="none"/></svg><br>Advanced Search
  </div>
  <h1><em>FIND</em> YOUR DOMAIN</h1>
  <h2>Your Business Starts Here</h2>
  <p class="intro">Lorem Ipsum is simply dummy text of the printing and typesetting industry. Lorem Ipsum has been the industry's standard dummy text ever since the 1500s, when an unknown printer.</p>
  <div class="search"><span class="placeholder">Enter your domain name</span><span class="tld">.COM <span>▾</span></span></div>
  <div class="search-btn">SEARCH</div>

  <div class="quote" style="left:126px">Parcel Names Group, LLC domain was very quick at responding to my questions and made it easy to work with them. I highly recommend using them to purchase any domain names.</div>
  <div class="quote-name" style="left:162px">Name Here<small>Company Name</small></div>
  <div class="quote" style="left:423px">Parcel Names Group, LLC domain was very quick at responding to my questions and made it easy to work with them. I highly recommend using them to purchase any domain names.</div>
  <div class="quote-name" style="left:460px">Name Here<small>Company Name</small></div>
  <div class="arrows">‹ ›</div>
</section>

<div class="feature" style="left:126px">
  <div class="icon"><svg width="16" height="16" viewBox="0 0 16 16"><circle cx="6" cy="6" r="3" fill="none" stroke="#fff" stroke-width="2"/><circle cx="11.5" cy="11.5" r="2" fill="none" stroke="#fff" stroke-width="1.5"/></svg></div>
  <h3>Strong<br>Keywords</h3>
  <p>Lorem Ipsum is simply dummy text of the printing and typesetting industry. Lorem Ipsum has been the industry's standard dummy...</p>
  <span class="more">more</span>
</div>
<div class="feature" style="left:270px">
  <div class="icon"><svg width="16" height="16" viewBox="0 0 16 16"><rect x="5" y="1" width="6" height="8" rx="3" fill="none" stroke="#fff" stroke-width="1.8" transform="rotate(30 8 8)"/><rect x="5" y="7" width="6" height="8" rx="3" fill="none" stroke="#fff" stroke-width="1.8" transform="rotate(30 8 8)"/></svg></div>
  <h3>Short<br>URL</h3>
  <p>Lorem Ipsum is simply dummy text of the printing and typesetting industry. Lorem Ipsum has been the industry's standard dummy...</p>
  <span class="more">more</span>
</div>
<div class="feature" style="left:414px">
  <div class="icon"><svg width="18" height="18" viewBox="0 0 18 18"><circle cx="9" cy="9" r="7.5" fill="none" stroke="#fff" stroke-width="1.8"/><circle cx="9" cy="4.5" r="1.8" fill="#fff"/><circle cx="9" cy="13.5" r="1.8" fill="#fff"/><circle cx="4.5" cy="9" r="1.8" fill="#fff"/><circle cx="13.5" cy="9" r="1.8" fill="#fff"/></svg></div>
  <h3>500+<br>BackLinks</h3>
  <p>Lorem Ipsum is simply dummy text of the printing and typesetting industry. Lorem Ipsum has been the industry's standard dummy...</p>
  <span class="more">more</span>
</div>
<div class="feature" style="left:557px">
  <div class="icon"><svg width="18" height="18" viewBox="0 0 18 18"><circle cx="9" cy="9" r="7.5" fill="#fff"/><path d="M9 9V1.5A7.5 7.5 0 0 1 15.5 12.7z" fill="#1d5aa6"/></svg></div>
  <h3>Quick<br>SEO Ranking</h3>
  <p>Lorem Ipsum is simply dummy text of the printing and typesetting industry. Lorem Ipsum has been the industry's standard dummy...</p>
  <span class="more">more</span>
</div>

<div class="abs welcome-title">Welcome to <b>ZEPRILO</b></div>
<div class="abs welcome-sub">The Identity Solution In Your Business</div>
<div class="abs cloud-art" role="img" aria-label="Illustration of a blue cloud with colourful domain extension signs"></div>
<p class="abs welcome-text">The inspiration for Zeprilo.com, Inc. was the realization that there is a need for a dedicated sales forum for Internet domain names featuring an experienced team of knowledgeable personnel who provide industry leading customer service while providing direct access to the best domains on the Internet.<br><a href="#">Learn More</a></p>

<section class="abs results">
  <h4>OUR RESULTS</h4>
  <p class="lead">See our total domain &amp; sell</p>
  <div class="stat">
    <div class="www">WWW</div>
    <div class="num">3,000,123</div>
    <div class="label">Total Domains</div>
    <div class="stat-rule"></div>
  </div>
  <div class="stat" style="margin-top:10px">
    <div class="www">WWW <span>SOLD</span></div>
    <div class="num">2,000,135</div>
    <div class="label">Total Sell Premium Domains</div>
  </div>
</section>
<div class="abs results-divider"></div>
<div class="abs tabs"><span class="on">Just Sold</span><span>New Added</span></div>
<table class="abs sales">
  <thead><tr><th>Date</th><th>Domain</th><th>Price</th></tr></thead>
  <tbody>
    <tr><td>30 Day</td><td>brushvale.example</td><td>$2,000</td></tr>
    <tr><td>30 Day</td><td>brushvale.example</td><td>$2,000</td></tr>
    <tr><td>30 Day</td><td>brushvale.example</td><td>$2,000</td></tr>
    <tr><td>30 Day</td><td>brushvale.example</td><td>$2,000</td></tr>
    <tr><td>30 Day</td><td>brushvale.example</td><td>$2,000</td></tr>
  </tbody>
</table>

<footer class="abs footer"></footer>
<div class="abs cta">
  <h5>Ready to start your business?</h5>
  <p>Just search yout desire domain name and build a website to grow your business</p>
  <div class="btn">Get Domain!</div>
</div>

<div class="fcol" style="left:125px"><h6>Deleting Domains</h6><ul><li>Traffic score</li><li>Domain rank</li><li>Popularity score</li><li>US based traffic percent</li></ul></div>
<div class="fsep" style="left:240px"></div>
<div class="fcol" style="left:254px"><h6>Domains For Sale</h6><ul><li>Premium Domains</li><li>Newest Domains</li><li>Elite Domains</li><li>Cheap Domains</li></ul></div>
<div class="fsep" style="left:362px"></div>
<div class="fcol" style="left:375px"><h6>Company</h6><ul><li>About Us</li><li>History</li><li>Support</li><li>Contact</li><li>FAQ</li></ul></div>
<div class="fsep" style="left:450px"></div>
<div class="fcol" style="left:463px"><h6>Contact Us</h6><address><b>ZEPRILO, Inc</b><br>48 Harbor Line Road<br>Suite 12<br>Fairview, ST 00410<br>United States<br><br>Phone: +1 555.014.2290</address></div>
<div class="fsep" style="left:563px"></div>
<div class="fcol newsletter" style="left:574px;width:122px"><h6>Newsletter</h6><p style="padding-left:7px">Sign up for a monthly newsletter</p><input type="text" placeholder="email here"><div class="submit">Submit</div></div>

<p class="abs copyright">Copyright 2013 Zeprilo.com, Inc. | Terms Of Use | Privacy Statement</p>
<div class="abs cards"><span></span><span></span><span></span><span></span><span></span></div>
<div class="abs connect">Connect - <i></i><i></i><i></i><i></i></div>

</body>
</html>
```